Classic Minimalistic Business Card

Design a classic, minimalistic Business Card. Please find inspiration in the attached Classic Minimalistic examples. My information:
Name: Glen Whitacre
Company: Whitacre Capital
Logo: WC
Address: 1800 N Corliss Ave, Suite 420 | Larkfield, WI 53187
Phone: 630-555-0172
Email: glenwhitacre@tvm.example
Slogan: Growing the Strength of Wealth

Feel free to leave out any of the information above except my name.

I have selected Double-sided, but I am also open to Single-sided

Target Market(s)

22-70. income greater than 150k/year

Industry/Entity Type

Finance

Contact Information for Business Card

See Project Description

Requirements
Must have
• Ivory or "antiqued" background similar to the reference pictures

```html
<!DOCTYPE html>
<html lang="en">
<head>
<meta charset="utf-8">
<title>Whitacre Capital – Business Card</title>
<link href="https://fonts.googleapis.com/css2?family=Mulish:wght@400;700&display=swap" rel="stylesheet">
<style>
  :root {
    --canvas: #efeae2;
    --card-ivory: #d9ceb3;
    --card-ivory-light: #e2d8c0;
    --card-ivory-dark: #cdbf9f;
    --ink: #1f1d1a;
    --ink-soft: #3a3733;
    --card-shadow: rgba(60, 45, 25, 0.18);
  }
  * { box-sizing: border-box; margin: 0; padding: 0; }
  html, body {
    width: 1200px;
    height: 800px;
    overflow: hidden;
    background: var(--canvas);
    font-family: "Mulish", sans-serif;
    color: var(--ink);
  }
  .canvas {
    position: relative;
    width: 1200px;
    height: 800px;
    display: flex;
    align-items: center;
    justify-content: center;
    gap: 60px;
  }
  .card {
    position: relative;
    width: 520px;
    height: 297px;
    background: radial-gradient(ellipse at 40% 35%, var(--card-ivory-light) 0%, var(--card-ivory) 60%, var(--card-ivory-dark) 100%);
    box-shadow: 0 10px 28px var(--card-shadow);
  }

  /* Contact side */
  .brand {
    position: absolute;
    top: 46px;
    left: 120px;
    white-space: nowrap;
  }
  .brand-name {
    font-size: 34px;
    font-weight: 400;
    letter-spacing: 0.5px;
    color: var(--ink);
    line-height: 1;
  }
  .brand-slogan {
    margin-top: 12px;
    margin-left: 64px;
    font-size: 13px;
    color: var(--ink-soft);
  }
  .contact {
    position: absolute;
    left: 44px;
    top: 150px;
    white-space: nowrap;
  }
  .contact-name {
    margin-left: 120px;
    font-size: 19px;
    font-weight: 700;
    color: var(--ink);
    margin-bottom: 12px;
  }
  .contact-line {
    font-size: 13.5px;
    color: var(--ink-soft);
    line-height: 1.55;
  }
  .contact-line .gap { display: inline-block; width: 18px; }

  /* Monogram side */
  .card-back {
    display: flex;
    align-items: center;
    justify-content: center;
  }
  .monogram {
    font-size: 96px;
    font-weight: 400;
    letter-spacing: 4px;
    color: var(--ink);
    line-height: 1;
  }
</style>
</head>
<body>
  <main class="canvas">
    <section class="card card-front" aria-label="Business card, contact side">
      <div class="brand">
        <p class="brand-name">Whitacre Capital</p>
        <p class="brand-slogan">Growing the Strength of Wealth</p>
      </div>
      <div class="contact">
        <p class="contact-name">Glen Whitacre</p>
        <p class="contact-line">1800 N Corliss Ave, Suite 420 | Larkfield, WI 53187</p>
        <p class="contact-line">630-555-0172<span class="gap"></span>glenwhitacre@tvm.example</p>
      </div>
    </section>

    <section class="card card-back" aria-label="Business card, monogram side">
      <p class="monogram">WC</p>
    </section>
  </main>
</body>
</html>
```